Auto glass company

BRIGHTWAY
Roving Auto Glass, LLC
555-604-1937

* Windshield Replacement
* Rock Chip Repair
Danny "K"
Brightwayrovingautoglass@example.com
* Fully Insured

This is what I would like on the card. The image is what I had before. Looking for a logo possible too, couldn’t find a place to add that on. It’s a auto glass company.

Target Market(s)

Auto glass

Industry/Entity Type

Auto glass

Contact Information for Business Card

Logo, business name, phone number, windshield replacement, rock chip repair, insured, owner name Danny K, email address brightwayrovingautoglass@example.com

Colors

Designer to choose colors to be used in the design.

Requirements
Must have
• Logo, business name, phone number, windshield replacement, rock chip repair, insured, owner name Danny K, email address brightwayrovingautoglass@example.com

```html
<!DOCTYPE html>
<html lang="en">
<head>
<meta charset="utf-8">
<title>Brightway Roving Auto Glass – Business Card</title>
<link href="https://fonts.googleapis.com/css2?family=Montserrat:wght@400;500;700;800&display=swap" rel="stylesheet">
<style>
  :root {
    --backdrop: #2b2b2d;
    --card: #1c1c1e;
    --blue: #2a8fd8;
    --text: #e9e9ea;
    --muted: #cfcfd2;
  }
  * { box-sizing: border-box; margin: 0; padding: 0; }
  html, body {
    width: 1200px; height: 1186px; overflow: hidden;
    background: var(--backdrop);
    font-family: "Montserrat", Arial, sans-serif;
    color: var(--text);
  }
  .canvas { position: relative; width: 1200px; height: 1186px; }
  .card {
    position: absolute; left: 150px;
    width: 900px; height: 514px;
    background: var(--card);
    border-radius: 34px;
    box-shadow: 0 18px 40px rgba(0,0,0,0.45);
  }
  .card--front { top: 52px; }
  .card--back { top: 620px; }

  .wordmark { position: absolute; font-weight: 800; color: var(--text); line-height: 1; }
  .wordmark__row { display: flex; align-items: center; gap: 18px; }
  .wordmark__square { width: 34px; height: 34px; background: var(--blue); flex: none; }
  .wordmark__name { letter-spacing: 4px; }
  .wordmark__sub { letter-spacing: 3px; text-transform: uppercase; margin-top: 14px; }

  .card--front .wordmark { left: 50%; top: 50%; transform: translate(-50%, -50%); }
  .card--front .wordmark__name { font-size: 68px; }
  .card--front .wordmark__sub { font-size: 22px; padding-left: 52px; }

  .card--back .wordmark { left: 90px; top: 92px; }
  .card--back .wordmark__name { font-size: 46px; }
  .card--back .wordmark__square { width: 26px; height: 26px; }
  .card--back .wordmark__sub { font-size: 15px; padding-left: 44px; margin-top: 10px; }

  .services {
    position: absolute; right: 70px; top: 200px;
    list-style: none; font-size: 19px; color: var(--muted); line-height: 1.6;
  }
  .services li { position: relative; padding-left: 22px; }
  .services li::before {
    content: ""; position: absolute; left: 0; top: 12px;
    width: 7px; height: 7px; border-radius: 50%; background: var(--blue);
  }

  .contact { position: absolute; left: 90px; bottom: 60px; }
  .contact__name { font-size: 30px; font-weight: 700; color: var(--blue); }
  .contact__role { font-size: 18px; color: var(--muted); margin-top: 4px; }
  .contact__rule { width: 22px; height: 2px; background: var(--blue); margin: 16px 0 14px; }
  .contact__line { display: flex; align-items: center; gap: 12px; font-size: 18px; color: var(--muted); margin-top: 6px; }
  .contact__icon { width: 16px; height: 16px; fill: var(--blue); flex: none; }
</style>
</head>
<body>
<main class="canvas">
  <section class="card card--front" aria-label="Card front">
    <div class="wordmark">
      <div class="wordmark__row"><span class="wordmark__square"></span><span class="wordmark__name">BRIGHTWAY</span></div>
      <div class="wordmark__sub">Roving Auto Glass, LLC</div>
    </div>
  </section>

  <section class="card card--back" aria-label="Card back">
    <div class="wordmark">
      <div class="wordmark__row"><span class="wordmark__square"></span><span class="wordmark__name">BRIGHTWAY</span></div>
      <div class="wordmark__sub">Roving Auto Glass, LLC</div>
    </div>

    <ul class="services">
      <li>Windshield Replacement</li>
      <li>Rock Chip Repair</li>
      <li>Fully Insured</li>
    </ul>

    <div class="contact">
      <p class="contact__name">Danny "K"</p>
      <p class="contact__role">CEO &amp; Founder</p>
      <div class="contact__rule"></div>
      <p class="contact__line">
        <svg class="contact__icon" viewBox="0 0 24 24" aria-hidden="true"><path d="M6.6 10.8a15.1 15.1 0 0 0 6.6 6.6l2.2-2.2a1 1 0 0 1 1-.25 11.4 11.4 0 0 0 3.6.57 1 1 0 0 1 1 1V20a1 1 0 0 1-1 1A17 17 0 0 1 3 4a1 1 0 0 1 1-1h3.5a1 1 0 0 1 1 1c0 1.25.2 2.45.57 3.57a1 1 0 0 1-.25 1z"/></svg>
        555-604-1937
      </p>
      <p class="contact__line">
        <svg class="contact__icon" viewBox="0 0 24 24" aria-hidden="true"><path d="M2 5h20v14H2z M2 5l10 8 10-8" fill="none" stroke="#2a8fd8" stroke-width="2"/></svg>
        Brightwayrovingautoglass@example.com
      </p>
    </div>
  </section>
</main>
</body>
</html>
```